CREATE A BUSINESS CARD FOR A BOAT CLEANING SERVICE

WE ARE STARTING A NEW BOAT CLEANING BUSINESS. WE DIVE UNDERWATER TO CLEAN BOAT HULLS, JETTIES, UNDERWATER STRUCTURES ETC. WE ARE LOOKING FOR AN UPPERMARKET MODERN LOGO AND BUSINESS CARD AS ALOT OF OUR TARGET MARKET WILL BE HIGH END. YOU HAVE TO DESIGN A BUSINESS CARD AND LOGO SEPERATELY .
THE BUSINESS CARD DIMESNION MUST BE STANDARD SIZE.
The standard dimensions of a printed business card are 3.5 x 2 inches

Target Market(s)

UNDERWATER SERVICED

Industry/Entity Type

Business

Contact Information for Business Card

HALDEN UNDERWATER SERVICES

Font styles to use
Serif

Colors

Designer to choose colors to be used in the design.

Requirements
Must have
• HALDEN
Nice to have
• dark
Should not have
• more than 3 colors

```html
<!DOCTYPE html>
<html lang="en">
<head>
<meta charset="utf-8">
<title>Halden Underwater Services – Business Cards</title>
<link href="https://fonts.googleapis.com/css2?family=Open+Sans:wght@400;600&display=swap" rel="stylesheet">
<style>
  :root {
    --backdrop: #d2d2de;
    --paper-light: #f4f4f4;
    --paper-light-edge: #bdbdbd;
    --ink-dark: #121212;
    --paper-dark: #1b1a26;
    --paper-dark-edge: #12111b;
    --ink-light: #f2f4f6;
    --aqua: #3fb6d6;
  }
  * { box-sizing: border-box; margin: 0; padding: 0; }
  html, body { width: 1200px; height: 1006px; overflow: hidden; }
  body {
    background: var(--backdrop);
    font-family: "Open Sans", sans-serif;
    position: relative;
  }
  .card {
    position: absolute;
    width: 700px;
    height: 400px;
    border-radius: 3px;
    box-shadow: 0 10px 24px rgba(40, 40, 60, 0.25);
  }
  .card--light {
    left: 140px; top: 70px;
    background: linear-gradient(170deg, var(--paper-light) 0%, #d4d4d4 55%, var(--paper-light-edge) 100%);
    color: var(--ink-dark);
    --accent: var(--ink-dark);
    --rule: var(--ink-dark);
  }
  .card--dark {
    left: 360px; top: 536px;
    background: linear-gradient(160deg, #24233a 0%, var(--paper-dark) 50%, var(--paper-dark-edge) 100%);
    color: var(--ink-light);
    --accent: var(--aqua);
    --rule: var(--aqua);
  }
  .brand {
    position: absolute;
    left: 150px; top: 70px;
    display: flex; align-items: center; gap: 18px;
  }
  .brand__mark {
    width: 96px; height: 96px; border-radius: 50%;
    background: var(--aqua);
  }
  .brand__name { line-height: 1; font-weight: 600; color: inherit; }
  .brand__main { display: block; font-size: 64px; letter-spacing: 1px; }
  .brand__sub { display: block; font-size: 19px; letter-spacing: 1px; margin-top: 6px; }
  .person {
    position: absolute;
    right: 430px; top: 262px;
    text-align: right;
  }
  .person__name { font-size: 26px; }
  .person__role { font-size: 17px; color: var(--accent); margin-top: -2px; }
  .divider {
    position: absolute;
    left: 300px; top: 215px;
    width: 2px; height: 150px;
    background: var(--rule);
  }
  .contacts {
    position: absolute;
    left: 322px; top: 218px;
    list-style: none;
    font-size: 18px;
    line-height: 29px;
  }
  .contacts li { display: flex; align-items: center; gap: 9px; }
  .contacts svg { width: 15px; height: 15px; flex: none; }
</style>
</head>
<body>

<section class="card card--light" aria-label="Business card, light version">
  <div class="brand">
    <span class="brand__mark" aria-hidden="true"></span>
    <span class="brand__name">
      <span class="brand__main">HALDEN</span>
      <span class="brand__sub">UNDERWATER SERVICES</span>
    </span>
  </div>
  <div class="person">
    <p class="person__name">Marc Ellery</p>
    <p class="person__role">Service Manager</p>
  </div>
  <span class="divider" aria-hidden="true"></span>
  <ul class="contacts">
    <li><svg viewBox="0 0 15 15"><rect width="15" height="15" rx="2" fill="currentColor"/><path d="M3 5h9v6H3z M3 5l4.5 3.5L12 5" fill="none" stroke="#eee" stroke-width="1"/></svg>info@haldendive.com</li>
    <li><svg viewBox="0 0 15 15"><rect width="15" height="15" rx="2" fill="currentColor"/><circle cx="7.5" cy="7.5" r="4" fill="none" stroke="#eee" stroke-width="1.2"/></svg>www.haldendive.com</li>
    <li><svg viewBox="0 0 15 15"><rect width="15" height="15" rx="2" fill="currentColor"/><path d="M4 3.5l2 .5.5 2-1 1a6 6 0 0 0 2.5 2.5l1-1 2 .5.5 2c-4 .5-8-3.5-7.5-7.5z" fill="#eee"/></svg>555-310-4821</li>
    <li><svg viewBox="0 0 15 15"><rect width="15" height="15" rx="2" fill="currentColor"/><rect x="5" y="3" width="5" height="9" rx="1" fill="none" stroke="#eee" stroke-width="1.2"/></svg>555-310-7734</li>
    <li><svg viewBox="0 0 15 15"><rect width="15" height="15" rx="2" fill="currentColor"/><path d="M7.5 12.5s-3.5-4-3.5-6.2a3.5 3.5 0 0 1 7 0c0 2.2-3.5 6.2-3.5 6.2z" fill="#eee"/></svg>1420 Harbor Way, Bayfield, CA. 90000</li>
  </ul>
</section>

<section class="card card--dark" aria-label="Business card, dark version">
  <div class="brand">
    <span class="brand__mark" aria-hidden="true"></span>
    <span class="brand__name">
      <span class="brand__main">HALDEN</span>
      <span class="brand__sub">UNDERWATER SERVICES</span>
    </span>
  </div>
  <div class="person">
    <p class="person__name">Marc Ellery</p>
    <p class="person__role">Service Manager</p>
  </div>
  <span class="divider" aria-hidden="true"></span>
  <ul class="contacts">
    <li><svg viewBox="0 0 15 15"><rect width="15" height="15" rx="2" fill="#9fd6e6"/><path d="M3 5h9v6H3z M3 5l4.5 3.5L12 5" fill="none" stroke="#1b1a26" stroke-width="1"/></svg>info@haldendive.com</li>
    <li><svg viewBox="0 0 15 15"><rect width="15" height="15" rx="2" fill="#9fd6e6"/><circle cx="7.5" cy="7.5" r="4" fill="none" stroke="#1b1a26" stroke-width="1.2"/></svg>www.haldendive.com</li>
    <li><svg viewBox="0 0 15 15"><rect width="15" height="15" rx="2" fill="#9fd6e6"/><path d="M4 3.5l2 .5.5 2-1 1a6 6 0 0 0 2.5 2.5l1-1 2 .5.5 2c-4 .5-8-3.5-7.5-7.5z" fill="#1b1a26"/></svg>555-310-4821</li>
    <li><svg viewBox="0 0 15 15"><rect width="15" height="15" rx="2" fill="#9fd6e6"/><rect x="5" y="3" width="5" height="9" rx="1" fill="none" stroke="#1b1a26" stroke-width="1.2"/></svg>555-310-7734</li>
    <li><svg viewBox="0 0 15 15"><rect width="15" height="15" rx="2" fill="#9fd6e6"/><path d="M7.5 12.5s-3.5-4-3.5-6.2a3.5 3.5 0 0 1 7 0c0 2.2-3.5 6.2-3.5 6.2z" fill="#1b1a26"/></svg>1420 Harbor Way, Bayfield, CA. 90000</li>
  </ul>
</section>

</body>
</html>
```